Organizational health infographic

I work as an independent contractor with a larger consulting firm named "the Lantern Works" https://www.lanternworks-example.com/ I need a simple infographic that visually explains the 3 stages of our client engagement, and their respective steps and objectives. Im inclined to use a "subway" map system design (Ive included a a draft overview of the content (in PPT and a PDF) and b) a few sample subway style infographics. I

Target Market(s)

CEOs and Human Resources Officers

Font styles to use
Sans Serif

Colors

Designer to choose colors to be used in the design.

Requirements
Must have
• my contact info
• mark elwin 555-384-9021
• mark.elwin@lanternworksadvisory-example.com
• lantern works logo (I put it near the top center part of the page). Logo and book pictures can be found on the website https://www.lanternworks-example.com
Nice to have
• 1) the more consistent the font and colors are with the Lantern Works website, the better https://www.lanternworks-example.com
• 2) if its possible to have all 3 "subway lines" collapse into a single timeline, that would be cool.
• 3) If its possible to add a visual timeline that shows each stage taking approx 3 to 6 months, also cool.
• 4) in stage 3, Im not sure about whether to use the actual book pictures or simply the titles of each book at a "subway stop" circle.

```html
<!DOCTYPE html>
<html lang="en">
<head>
<meta charset="utf-8">
<title>Lantern Works – Engagement Stages</title>
<link rel="stylesheet" href="https://fonts.googleapis.com/css2?family=Montserrat:wght@400;500;700&display=swap">
<style>
  :root {
    --red: #c41f3a;
    --navy: #1f2433;
    --white: #ffffff;
    --track: #f3dfe3;
    --ink: #2b2f3c;
    --silver: #d9d9dc;
    --gold: #c7a24a;
    --cream: #f1ede4;
  }
  html, body {
    margin: 0;
    padding: 0;
    overflow: hidden;
    background: var(--white);
  }
  .canvas {
    position: relative;
    width: 782px;
    height: 1200px;
    overflow: hidden;
    background: var(--white);
    font-family: "Montserrat", sans-serif;
  }
  .band { position: absolute; left: 0; width: 782px; }
  .band--stage1 { top: 70px; height: 312px; background: var(--red); }
  .band--stage2 { top: 394px; height: 376px; background: var(--navy); }
  .band--stage3 { top: 782px; height: 320px; background: var(--red); }
  .band--legend { top: 1114px; height: 86px; background: var(--navy); }

  .brand {
    position: absolute; top: 12px; left: 0; width: 782px;
    display: flex; justify-content: center; align-items: center; gap: 10px;
  }
  .brand__dot { width: 30px; height: 30px; border-radius: 50%; background: var(--red); }
  .brand__name { font-size: 34px; font-weight: 500; color: var(--ink); letter-spacing: -0.5px; }

  .map { position: absolute; top: 0; left: 0; }
  .map text { font-family: "Montserrat", sans-serif; fill: var(--white); }
  .stage-num { font-size: 12px; font-weight: 700; }
  .stage-title { font-size: 15px; font-weight: 700; }
  .duration { font-size: 12px; }
  .stop-label { font-size: 12.5px; text-anchor: middle; }
  .col-head { font-size: 13px; }
  .col-item { font-size: 11.2px; }
  .legend-title { font-size: 14px; font-weight: 700; }
  .legend-item { font-size: 12.5px; }
  .contact { font-size: 11.5px; }
  .track { stroke: var(--track); stroke-width: 8; fill: none; stroke-linecap: round; stroke-linejoin: round; }
  .station { fill: var(--red); stroke: var(--white); stroke-width: 2.5; }
  .station--navy { fill: var(--navy); }
  .stop { fill: var(--white); }
  .tick { stroke: var(--white); stroke-width: 1.2; }
  .connector { stroke: var(--white); stroke-width: 1.2; stroke-dasharray: 5 4; fill: none; }
  .col-box { fill: none; stroke: var(--white); stroke-width: 1.2; }
  .rule { stroke: var(--white); stroke-width: 1.5; }
  .bullet--dark { fill: var(--navy); }
  .bullet--red { fill: var(--red); }
</style>
</head>
<body>
<div class="canvas">
  <header class="brand">
    <span class="brand__dot"></span>
    <span class="brand__name">lantern works</span>
  </header>

  <div class="band band--stage1"></div>
  <div class="band band--stage2"></div>
  <div class="band band--stage3"></div>
  <div class="band band--legend"></div>

  <svg class="map" width="782" height="1200" viewBox="0 0 782 1200">
    <!-- Stage 1 -->
    <g class="stage stage--1">
      <text class="stage-num" x="34" y="92">Stage 1</text>
      <text class="stage-title" x="34" y="111">Executive Launch</text>
      <line class="rule" x1="26" y1="118" x2="182" y2="118"/>
      <text class="duration" x="38" y="137">3 to 6 months</text>

      <line class="track" x1="78" y1="246" x2="420" y2="246"/>
      <circle class="station" cx="78" cy="246" r="22"/>
      <circle class="stop" cx="156" cy="246" r="11"/>
      <circle class="stop" cx="232" cy="246" r="11"/>
      <circle class="station" cx="320" cy="246" r="22"/>
      <polygon fill="#ffffff" points="412,226 448,246 412,266"/>

      <line class="tick" x1="156" y1="206" x2="156" y2="235"/>
      <line class="tick" x1="320" y1="196" x2="320" y2="224"/>
      <line class="tick" x1="78" y1="268" x2="78" y2="286"/>
      <line class="tick" x1="232" y1="257" x2="232" y2="278"/>
      <text class="stop-label" x="156" y="202">Meeting Audits</text>
      <text class="stop-label" x="320" y="192">Quarterly Offsites</text>
      <text class="stop-label" x="78" y="304">2 Day</text>
      <text class="stop-label" x="232" y="295">Leader Coaching</text>

      <polyline class="connector" points="458,246 486,246 486,364 90,364 90,402"/>

      <rect class="col-box" x="524" y="82" width="130" height="28"/>
      <text class="col-head" x="541" y="101">Objectives</text>
      <circle class="bullet--dark" cx="530" cy="124" r="3"/>
      <text class="col-item" x="540" y="128">Team cohesion</text>
      <text class="col-item" x="554" y="144">- Solid trust</text>
      <text class="col-item" x="554" y="160">- Aligned  expectations</text>
      <circle class="bullet--dark" cx="530" cy="171" r="3"/>
      <text class="col-item" x="540" y="175">Playbook 1.0</text>
      <text class="col-item" x="554" y="191">- Aligned vision, values, strategy,</text>
      <text class="col-item" x="562" y="206">priorities &amp; roles</text>
      <circle class="bullet--dark" cx="530" cy="219" r="3"/>
      <text class="col-item" x="540" y="223">Productive meetings</text>
      <circle class="bullet--dark" cx="530" cy="235" r="3"/>
      <text class="col-item" x="540" y="239">Consistent communication with</text>
      <text class="col-item" x="540" y="254">greater org</text>

      <rect class="col-box" x="524" y="275" width="158" height="29"/>
      <text class="col-head" x="541" y="294">Transition readiness</text>
      <circle class="bullet--dark" cx="530" cy="321" r="3"/>
      <text class="col-item" x="540" y="325">Cohesion validation (CTAR)</text>
      <circle class="bullet--dark" cx="530" cy="338" r="3"/>
      <text class="col-item" x="540" y="342">Playbook complete</text>
      <circle class="bullet--dark" cx="530" cy="355" r="3"/>
      <text class="col-item" x="540" y="359">Meeting momentum</text>
    </g>

    <!-- Stage 2 -->
    <g class="stage stage--2">
      <line class="connector" x1="90" y1="480" x2="90" y2="566"/>
      <text class="stage-num" x="34" y="422">Stage 2</text>
      <text class="stage-title" x="34" y="441">Next Level Rollout</text>
      <line class="rule" x1="26" y1="449" x2="220" y2="449"/>
      <text class="duration" x="38" y="470">3 to 6 months</text>

      <polyline class="track" points="90,588 152,524 336,524 400,588"/>
      <polyline class="track" points="90,588 152,654 336,654 400,588"/>
      <line class="track" x1="400" y1="588" x2="420" y2="588"/>
      <circle class="station station--navy" cx="90" cy="588" r="22"/>
      <circle class="station station--navy" cx="152" cy="524" r="22"/>
      <circle class="station station--navy" cx="245" cy="524" r="22"/>
      <circle class="station station--navy" cx="336" cy="524" r="22"/>
      <circle class="station station--navy" cx="152" cy="654" r="22"/>
      <circle class="stop" cx="214" cy="654" r="11"/>
      <circle class="stop" cx="269" cy="654" r="11"/>
      <circle class="station station--navy" cx="336" cy="654" r="22"/>
      <polygon fill="#ffffff" points="412,568 448,588 412,608"/>

      <text class="stop-label" x="245" y="492">Key Leader Conferences</text>
      <line class="tick" x1="214" y1="616" x2="214" y2="643"/>
      <text class="stop-label" x="214" y="612">Meeting Audits</text>
      <text class="stop-label" x="80" y="648">Key Leader</text>
      <text class="stop-label" x="80" y="664">Kickoff</text>
      <line class="tick" x1="152" y1="676" x2="152" y2="697"/>
      <text class="stop-label" x="152" y="714">Department</text>
      <text class="stop-label" x="152" y="730">Teams</text>
      <line class="tick" x1="269" y1="665" x2="269" y2="686"/>
      <text class="stop-label" x="269" y="702">Leader</text>
      <text class="stop-label" x="269" y="718">Coaching</text>
      <line class="tick" x1="336" y1="676" x2="336" y2="697"/>
      <text class="stop-label" x="367" y="716">Department</text>
      <text class="stop-label" x="367" y="732">Rollouts</text>

      <polyline class="connector" points="458,588 486,588 486,756 94,756 94,790"/>

      <rect class="col-box" x="524" y="420" width="130" height="29"/>
      <text class="col-head" x="541" y="439">Objectives</text>
      <circle class="bullet--red" cx="530" cy="474" r="3"/>
      <text class="col-item" x="540" y="478">Key leaders</text>
      <text class="col-item" x="550" y="496">- Finish  Playbook 2.0</text>
      <text class="col-item" x="550" y="513">- Become Ambassadors of Org Health</text>
      <text class="col-item" x="550" y="530">- Cross functional cooperation</text>
      <circle class="bullet--red" cx="530" cy="546" r="3"/>
      <text class="col-item" x="540" y="550">Department teams</text>
      <text class="col-item" x="550" y="566">- Cohesion, Clarity, productive meetings</text>
      <circle class="bullet--red" cx="530" cy="593" r="3"/>
      <text class="col-item" x="540" y="597">Department rollouts</text>
      <text class="col-item" x="550" y="613">- Break down silos</text>
      <text class="col-item" x="550" y="629">- Dept priorities  align to org priorities</text>

      <rect class="col-box" x="524" y="644" width="158" height="29"/>
      <text class="col-head" x="541" y="663">Transition readiness</text>
      <circle class="bullet--red" cx="530" cy="690" r="3"/>
      <text class="col-item" x="540" y="694">Department CTARs</text>
      <circle class="bullet--red" cx="530" cy="706" r="3"/>
      <text class="col-item" x="540" y="710">Core values detailed and implemented</text>
      <circle class="bullet--red" cx="530" cy="722" r="3"/>
      <text class="col-item" x="540" y="726">Meeting mastery</text>
    </g>

    <!-- Stage 3 -->
    <g class="stage stage--3">
      <line class="connector" x1="94" y1="866" x2="94" y2="962"/>
      <text class="stage-num" x="34" y="807">Stage 3</text>
      <text class="stage-title" x="34" y="827">Organizational Rollout</text>
      <line class="rule" x1="26" y1="835" x2="232" y2="835"/>
      <text class="duration" x="38" y="854">3 to 6 months</text>

      <polyline class="track" points="94,984 152,911 192,911"/>
      <polyline class="track" points="94,984 158,1050"/>
      <line class="track" x1="175" y1="1039" x2="320" y2="1039"/>
      <line class="track" x1="175" y1="1061" x2="320" y2="1061"/>
      <circle class="station" cx="94" cy="984" r="22"/>
      <rect class="station" x="135" y="894" width="34" height="34"/>
      <rect class="station" x="141" y="1033" width="34" height="34"/>

      <text class="stop-label" x="156" y="882">Workshops</text>
      <text class="stop-label" x="202" y="1005">Internal Training</text>
      <text class="stop-label" x="80" y="1049">Playbook</text>
      <text class="stop-label" x="80" y="1065">Rollout</text>
      <text class="col-item" x="194" y="1033">Train the Trainers</text>
      <text class="col-item" x="194" y="1056">Train the Leaders</text>

      <g role="img" aria-label="Covers of four leadership books used in the workshops">
        <rect x="186" y="894" width="42" height="66" fill="#a8182e"/>
        <rect x="244" y="894" width="40" height="66" fill="var(--silver)"/>
        <rect x="294" y="894" width="42" height="66" fill="var(--cream)"/>
        <rect x="343" y="894" width="43" height="66" fill="var(--gold)"/>
      </g>
      <rect role="img" aria-label="Cover of the team workbook used for internal training" x="318" y="998" width="78" height="92" fill="#b51b33" stroke="#e9c7cd" stroke-width="1"/>

      <rect class="col-box" x="524" y="822" width="130" height="29"/>
      <text class="col-head" x="541" y="841">Objectives</text>
      <circle class="bullet--dark" cx="544" cy="874" r="3"/>
      <text class="col-item" x="554" y="878">All employees</text>
      <text class="col-item" x="562" y="894">- Understand and utilize the Playbook</text>
      <text class="col-item" x="562" y="911">- Are equipped &amp; motivated to create</text>
      <text class="col-item" x="570" y="926">a healthy culture</text>

      <rect class="col-box" x="524" y="956" width="158" height="29"/>
      <text class="col-head" x="541" y="975">Transition readiness</text>
      <circle class="bullet--dark" cx="544" cy="999" r="3"/>
      <text class="col-item" x="554" y="1003">The consultation is completed when</text>
      <text class="col-item" x="554" y="1019">the leaders are ready to assume</text>
      <text class="col-item" x="554" y="1034">responsibility for maintaining a healthy</text>
      <text class="col-item" x="554" y="1051">culture.</text>
    </g>

    <!-- Legend -->
    <g class="legend">
      <text class="legend-title" x="36" y="1138">Legend</text>
      <circle cx="48" cy="1166" r="11" fill="var(--red)" stroke="#ffffff" stroke-width="1.5"/>
      <text class="legend-item" x="68" y="1170">Live off</text>
      <text class="legend-item" x="68" y="1186">site</text>
      <circle class="stop" cx="162" cy="1166" r="6"/>
      <text class="legend-item" x="176" y="1170">Video</text>
      <text class="legend-item" x="176" y="1186">conference</text>
      <polygon fill="#ffffff" points="276,1154 296,1166 276,1178"/>
      <text class="legend-item" x="306" y="1162">Transition</text>
      <text class="legend-item" x="306" y="1178">Evaluation</text>
      <rect x="402" y="1157" width="18" height="18" fill="var(--red)" stroke="#ffffff" stroke-width="1.5"/>
      <text class="legend-item" x="430" y="1170">Training</text>
      <text class="contact" x="510" y="1158">mark elwin 555-384-9021</text>
      <text class="contact" x="510" y="1176" textLength="262" lengthAdjust="spacingAndGlyphs">mark.elwin@lanternworksadvisory-example.com</text>
    </g>
  </svg>
</div>
</body>
</html>
```